Web Design For Coral Basin Pool Service

We are working with a company that wants a website for their pool service. Some sites to use for content/competitors and inspiration:
https://sacramento.lumawaterworks.example/builder/newbuild/repair/ppc
https://orchardsplashcareplus.example/
https://bluefinaquacare.example/
https://www.halvorsenplasterworks.example/pool-renovation-ga/
Thank you for taking the time to consider designing a website for us. We are web developers based in Stockton, CA, USA. Most of our projects go through the same process. Understanding this process may help you win a project with us. We custom-code all of our websites in-house. We don’t have any requirements as to what tools you use for your design, but we prefer Figma files. For any design that we label as four-stars, we send it to the client for review. The client picks the final design they want us to use. Once we complete this process, we will continue to show additional clients all the four-star sites and purchase them later. Your designs will have multiple chances to sell. For better chances of success, we ask that you follow these guidelines.
IMAGES:
If you use any images or icons in the design, we ask that you have a link to the asset so we can purchase the image/icon. Most of the designs we submit do not have the customer’s images on them unless they have some great images. Be creative; show us the feeling you are trying to portray with your image choices. Use any royalty-free site you choose. We subscribe to Adobe and mainly use their images, but we can purchase images outside of Adobe. PLEASE NOTE: we will not submit designs to clients with watermarks on the images.
FONTS:
We ask that you identify the fonts used in the design. This can be done in a message if you want. We typically use Google Fonts and Adobe Fonts.
CONTENT:
We're always open to different content and ideas. We often submit designs with stock images so the client can see our vision. We typically take pictures after the website launch to use their images with our vision. Lorem Ipsum is fine for paragraphs, but we ask that you write the headers in correct English. We want to be able to show the vision and identify the sections of the website.
INSPIRATION:
We typically add a couple of links in the brief of websites we like to help you get started in your design.
REVISIONS:
We do not often ask for revisions of the designs unless we see something in the design that may not appeal to the client. If there are slight changes that we want to make, we do that in the development process.
FEEDBACK:
We rarely give feedback on designs during the design process. We are working on many website projects and do not have the time to provide feedback. We usually respond if your request is well thought out and asks specific questions, but a note asking “feedback, please” usually goes unanswered.

```html
<!DOCTYPE html>
<html lang="en">
<head>
<meta charset="utf-8">
<title>Coral Basin Pool Service</title>
<link href="https://fonts.googleapis.com/css2?family=Open+Sans:wght@400;600;700&display=swap" rel="stylesheet">
<style>
:root{
  --navy:#0b2650;
  --navy-deep:#08204a;
  --heading:#143a6e;
  --blue:#2a9df4;
  --text:#4a4f57;
  --light:#f3f4f5;
  --white:#ffffff;
}
*{margin:0;padding:0;box-sizing:border-box}
html,body{width:1200px;height:4371px;overflow:hidden}
body{position:relative;font-family:"Open Sans",sans-serif;color:var(--text);background:var(--white)}
.abs{position:absolute}
.btn{position:absolute;background:var(--blue);color:var(--white);font-weight:700;font-size:13px;display:flex;align-items:center;justify-content:center;letter-spacing:.3px}
.eyebrow{position:absolute;color:var(--blue);font-weight:700;font-size:16px}
.h2{position:absolute;color:var(--heading);font-weight:700;font-size:46px;line-height:56px;letter-spacing:.5px}
.para{position:absolute;font-size:14px;line-height:24.5px;color:var(--text)}

/* top bar & header */
.topbar{left:390px;top:0;width:810px;height:31px;background:var(--navy);color:var(--white);font-size:11px;font-weight:600}
.topbar .item{position:absolute;top:0;height:31px;display:flex;align-items:center;gap:8px}
.topbar .appt{left:202px;width:234px;background:var(--blue);justify-content:center}
.brand{font-weight:700;font-size:22px;color:var(--heading);letter-spacing:.5px}
.nav a{position:absolute;top:58px;font-size:11px;font-weight:600;color:#222;text-decoration:none}
.contact-btn{left:930px;top:53px;width:119px;height:28px;border:1.5px solid #f0a24a;border-radius:3px;color:#f0a24a;font-size:10px;display:flex;align-items:center;justify-content:center}

/* hero */
.hero{left:0;top:98px;width:1200px;height:734px;background:linear-gradient(160deg,#6b6f68 0%,#8a7a62 35%,#4d4a44 70%,#2f2e2c 100%)}
.hero-welcome{left:110px;top:259px;color:var(--white);font-size:13px;display:flex;align-items:center;gap:12px}
.hero-welcome span{width:45px;height:1px;background:var(--white)}
.hero-title{left:110px;top:286px;color:var(--white);font-size:44px;font-weight:700;line-height:57px;letter-spacing:.5px}
.hero-text{left:110px;top:418px;width:420px;color:var(--white);font-size:13.5px;line-height:21px}

/* services */
.services{left:0;top:1442px;width:1200px;height:647px;background:var(--navy-deep)}
.svc-card{position:absolute;top:1733px;width:321px;height:242px;border-radius:4px}
.svc-ring{position:absolute;width:98px;height:98px;border-radius:50%;border:1px solid rgba(255,255,255,.3)}
.svc-icon{position:absolute;width:80px;height:80px;border-radius:50%;background:var(--blue);display:flex;align-items:center;justify-content:center}
.svc-label{position:absolute;top:1943px;width:287px;height:77px;background:var(--white);border-radius:3px;text-align:center;box-shadow:0 4px 14px rgba(0,0,0,.12)}
.svc-label h3{font-size:17px;font-weight:700;color:var(--heading);margin-top:13px}
.svc-label p{font-size:13px;color:#555;margin-top:4px}

/* why */
.why{left:0;top:2089px;width:1200px;height:623px;background:var(--light)}
.tab{position:absolute;top:2350px;height:45px;background:var(--white);color:var(--blue);font-weight:700;font-size:15px;display:flex;align-items:center;justify-content:center;border-radius:3px}
.tab.active{background:var(--blue);color:var(--white)}
.check{position:absolute;left:368px;font-size:13px;display:flex;align-items:center;gap:10px}

/* band */
.band{left:0;top:2712px;width:1200px;height:436px;background:linear-gradient(100deg,#1d1b1a 0%,#2c2926 50%,#1b1a19 100%)}
.pill{position:absolute;left:691px;width:393px;height:47px;border-radius:8px;background:rgba(255,255,255,.16);color:var(--white);font-size:12px;font-weight:700;display:flex;align-items:center;padding-left:53px}

/* reviews */
.reviews{left:0;top:3148px;width:1200px;height:700px;background:var(--light)}
.rv-photo{position:absolute;top:3374px;width:89px;height:122px}
.rv-card{position:absolute;top:3477px;width:302px;height:163px;background:var(--white);box-shadow:0 4px 16px rgba(0,0,0,.06);padding:35px 25px 0 30px;font-size:13px;line-height:24px}
.rv-name{position:absolute;top:3395px;font-size:17px;font-weight:600;color:#333}
.rv-role{position:absolute;top:3425px;font-size:12px;color:#555}
.rv-quote{position:absolute;top:3462px;color:var(--blue);font-size:70px;font-weight:700;line-height:70px}

/* footer */
.footer{left:0;top:4030px;width:1200px;height:341px;background:var(--navy)}
.ft-h{position:absolute;top:4050px;color:var(--white);font-size:19px;font-weight:700}
.social{position:absolute;top:4236px;width:31px;height:31px;border-radius:3px;background:rgba(255,255,255,.22)}
</style>
</head>
<body>

<!-- top bar -->
<div class="abs topbar">
  <div class="item" style="left:55px">
    <svg width="14" height="14" viewBox="0 0 24 24" fill="none" stroke="#fff" stroke-width="2"><path d="M22 16.9v3a2 2 0 0 1-2.2 2A19.8 19.8 0 0 1 2.1 4.2 2 2 0 0 1 4.1 2h3a2 2 0 0 1 2 1.7c.1.9.4 1.8.7 2.7a2 2 0 0 1-.5 2.1L8 9.8a16 16 0 0 0 6 6l1.3-1.3a2 2 0 0 1 2.1-.4c.9.3 1.8.6 2.7.7a2 2 0 0 1 1.7 2z"/></svg>
    555 - 014 - 2280
  </div>
  <div class="item appt">
    <svg width="13" height="13" viewBox="0 0 24 24" fill="none" stroke="#fff" stroke-width="2"><rect x="3" y="5" width="18" height="16" rx="2"/><path d="M3 10h18M8 3v4M16 3v4"/></svg>
    REQUEST AN APPOINTMENT
  </div>
  <div class="item" style="left:467px;font-size:10px">
    <svg width="12" height="14" viewBox="0 0 24 24" fill="none" stroke="#fff" stroke-width="2"><path d="M12 22s7-7 7-12a7 7 0 0 0-14 0c0 5 7 12 7 12z"/><circle cx="12" cy="10" r="2.5"/></svg>
    1234 Lagoon Way Somewhere
  </div>
</div>

<!-- header -->
<div class="abs brand" style="left:122px;top:48px;font-size:18px">Coral Basin Pool Service</div>
<nav class="nav">
  <a style="left:395px">Home</a>
  <a style="left:470px">About Us</a>
  <a style="left:545px">Services</a>
  <a style="left:633px">Gallery</a>
  <a style="left:726px">Our Team</a>
</nav>
<div class="abs contact-btn">CONTACT US</div>

<!-- hero -->
<div class="abs hero" role="img" aria-label="Children running toward a backyard pool at sunset"></div>
<svg class="abs" style="left:0;top:602px" width="1200" height="232" viewBox="0 0 1200 232">
  <path d="M0,232 L0,60 C300,150 520,232 800,226 C1000,214 1150,100 1200,28 L1200,232 Z" fill="#fff"/>
  <path d="M0,52 C150,110 300,160 420,196 C300,180 150,145 0,100 Z" fill="#2a9df4"/>
  <path d="M1200,18 C1130,110 1060,160 990,194 C1080,162 1150,112 1200,72 Z" fill="#2a9df4"/>
</svg>
<div class="abs hero-welcome">Welcome <span></span></div>
<h1 class="abs hero-title">Crafting Memories,<br>One Pool at a Time</h1>
<p class="abs hero-text">Lorem ipsum dolor sit amet, consectetur adipiscing elit, sed do eiusmod tempor incididunt ut labore et dolore magna Lorem ipsum dolor sit amet, consectetur adipiscing elit, sed do eiusmod tempor incididunt ut labore et dolore magna</p>
<div class="btn" style="left:110px;top:533px;width:192px;height:39px">Discover more</div>

<!-- about -->
<div class="abs" style="left:101px;top:883px;width:464px;height:464px;clip-path:polygon(50% 0,100% 50%,50% 100%,0 50%);background:linear-gradient(135deg,#8a5a4a 0%,#3aa3d8 45%,#1f6fa8 70%,#9fa9b2 100%)" role="img" aria-label="Collage of pool scenes: friends in a pool, a float, a deck and a villa pool"></div>
<div class="abs" style="left:291px;top:1073px;width:84px;height:84px;border-radius:50%;background:#fff;box-shadow:0 0 0 6px rgba(255,255,255,.4)"></div>
<div class="eyebrow" style="left:636px;top:920px">Who We Are</div>
<h2 class="h2" style="left:636px;top:952px">Crafting Aquatic<br>Masterpieces</h2>
<p class="para" style="left:639px;top:1068px;width:460px">Lorem ipsum dolor sit amet, consectetur adipiscing elit, sed do eiusmod tempor incididunt ut labore et dolore magna aliqua.Lorem ipsum dolor sit amet. Lorem ipsum dolor sit amet, consectetur adip iscing elit, sed do eiusmod tempor incididunt</p>
<p class="para" style="left:639px;top:1180px;width:460px">Lorem ipsum dolor sit amet, consectetur adipiscing elit, sed do eiusmod tempor incididunt ut labore et dolore magna aliqua.Lorem ipsum dolor sit amet. Lorem ipsum dolor sit amet, consectetur adip iscing elit, sed do eiusmod tempor incididunt</p>
<div class="btn" style="left:636px;top:1305px;width:150px;height:49px;font-size:14px">VIEW MORE</div>

<!-- services -->
<div class="abs services"></div>
<div class="abs" style="left:0;top:1538px;width:1200px;text-align:center;color:#fff;font-size:15px;font-weight:600">What We Do</div>
<div class="abs" style="left:0;top:1568px;width:1200px;text-align:center;color:#fff;font-size:44px;font-weight:700;letter-spacing:.5px">Services We Provide</div>

<div class="svc-card" style="left:93px;background:linear-gradient(160deg,#3d8fc4,#2a6f9e 60%,#1d4f78)" role="img" aria-label="Technician repairing pool tiles"></div>
<div class="svc-card" style="left:439px;background:linear-gradient(160deg,#b9c2c9,#8a9a6a 55%,#5e6a58)" role="img" aria-label="Construction crew in hard hats and safety vests"></div>
<div class="svc-card" style="left:779px;background:linear-gradient(160deg,#7fa370,#3ab0d6 55%,#2a8fbf)" role="img" aria-label="Family relaxing on floats in a clean pool"></div>

<div class="svc-ring" style="left:205px;top:1679px"></div><div class="svc-icon" style="left:214px;top:1688px"><svg width="36" height="36" viewBox="0 0 24 24" fill="none" stroke="#fff" stroke-width="1.5"><path d="M12 3l8 6-3 10H7L4 9z"/><circle cx="12" cy="3" r="1.5"/><circle cx="20" cy="9" r="1.5"/><circle cx="4" cy="9" r="1.5"/></svg></div>
<div class="svc-ring" style="left:550px;top:1679px"></div><div class="svc-icon" style="left:559px;top:1688px"><svg width="36" height="36" viewBox="0 0 24 24" fill="none" stroke="#fff" stroke-width="1.5"><path d="M4 20h16M8 16l8-10M13 4l4 4M6 20c0-3 2-4 4-4"/></svg></div>
<div class="svc-ring" style="left:890px;top:1679px"></div><div class="svc-icon" style="left:899px;top:1688px"><svg width="36" height="36" viewBox="0 0 24 24" fill="none" stroke="#fff" stroke-width="1.5"><circle cx="9" cy="8" r="3"/><circle cx="16" cy="9" r="2.5"/><path d="M3 19c0-3 3-5 6-5s6 2 6 5M15 14c3 0 6 1.5 6 4.5"/></svg></div>

<div class="svc-label" style="left:110px"><h3>Pool Repair</h3><p>Read more &#8594;</p></div>
<div class="svc-label" style="left:455px"><h3>Pool Construction</h3><p>Read more &#8594;</p></div>
<div class="svc-label" style="left:797px"><h3>Pool Cleaning</h3><p>Read more &#8594;</p></div>

<!-- why choose us -->
<div class="abs why"></div>
<div class="abs" style="left:755px;top:2164px;width:445px;height:548px;background:linear-gradient(170deg,#e9ecee 0%,#c9d4c2 40%,#b7c96a 75%,#8ea34d 100%)" role="img" aria-label="Two smiling engineers in hard hats holding plans"></div>
<div class="eyebrow" style="left:115px;top:2188px">Why Choose Us</div>
<h2 class="h2" style="left:115px;top:2219px">Making Waves with<br>Excellence</h2>
<div class="tab active" style="left:105px;width:127px">Our Mission</div>
<div class="tab" style="left:249px;width:116px">Our Vision</div>
<div class="tab" style="left:382px;width:124px">Our History</div>
<div class="abs" style="left:105px;top:2415px;width:223px;height:229px;border-radius:3px;background:linear-gradient(160deg,#3a3f44,#8c949a 50%,#b5c65a 100%)" role="img" aria-label="Engineers reviewing plans on site"></div>
<p class="para" style="left:368px;top:2435px;width:300px;font-size:13.5px">Lorem ipsum dolor sit amet, consectetur eiusmod tempor incididunt ut labore et do ipsum dolor sit amet. Lorem ipsum dolor si</p>
<div class="check" style="top:2536px"><svg width="15" height="15" viewBox="0 0 24 24" fill="none" stroke="#2a9df4" stroke-width="2"><rect x="3" y="3" width="18" height="18" rx="2"/><path d="M7 12l4 4 7-8"/></svg>Award Winning Company</div>
<div class="check" style="top:2570px"><svg width="15" height="15" viewBox="0 0 24 24" fill="none" stroke="#2a9df4" stroke-width="2"><rect x="3" y="3" width="18" height="18" rx="2"/><path d="M7 12l4 4 7-8"/></svg>Award Winning Company</div>
<div class="check" style="top:2604px"><svg width="15" height="15" viewBox="0 0 24 24" fill="none" stroke="#2a9df4" stroke-width="2"><rect x="3" y="3" width="18" height="18" rx="2"/><path d="M7 12l4 4 7-8"/></svg>Award Winning Company</div>

<!-- inspired band -->
<div class="abs band" role="img" aria-label="Modern house with a pool at dusk"></div>
<h2 class="abs" style="left:109px;top:2812px;color:#fff;font-size:45px;font-weight:700;line-height:56px;letter-spacing:.5px">Inspired Designs,<br>Impeccable<br>Craftsmanship</h2>
<div class="btn" style="left:109px;top:3004px;width:149px;height:41px;font-size:14px">GET STARTED</div>
<div class="pill" style="top:2841px">We've expert and certified staff</div>
<div class="pill" style="top:2907px">We've expert and certified staff</div>
<div class="pill" style="top:2971px">We've expert and certified staff</div>

<!-- reviews -->
<div class="abs reviews"></div>
<div class="eyebrow" style="left:0;top:3236px;width:1187px;text-align:center">Testimonials</div>
<h2 class="h2" style="left:0;top:3268px;width:1203px;text-align:center">Client Reviews</h2>

<div class="rv-photo" style="left:93px;background:linear-gradient(170deg,#e6e3df,#7b6a58 60%,#1d1f24)" role="img" aria-label="Client portrait"></div>
<div class="rv-name" style="left:200px">Marcus Delwyn</div><div class="rv-role" style="left:202px">CEO &amp; Founder</div>
<div class="rv-card" style="left:112px">Lorem ipsum dolor sit amet, consect etur adipiscing elit, sed do eiusmod tempor incididunt ut labore et dolore magna aliqua.Lorem ipsum dolor sit amet.</div>
<div class="rv-quote" style="left:352px">&#8220;</div>

<div class="rv-photo" style="left:439px;background:linear-gradient(170deg,#e9e6e1,#a88e6c 60%,#5a4a3a)" role="img" aria-label="Client portrait"></div>
<div class="rv-name" style="left:546px">Marcus Delwyn</div><div class="rv-role" style="left:548px">CEO &amp; Founder</div>
<div class="rv-card" style="left:458px">Lorem ipsum dolor sit amet, consect etur adipiscing elit, sed do eiusmod tempor incididunt ut labore et dolore magna aliqua.Lorem ipsum dolor sit amet.</div>
<div class="rv-quote" style="left:698px">&#8220;</div>

<div class="rv-photo" style="left:784px;background:linear-gradient(170deg,#3d4046,#5d6c80 60%,#2a3040)" role="img" aria-label="Client portrait"></div>
<div class="rv-name" style="left:892px">Marcus Delwyn</div><div class="rv-role" style="left:894px">CEO &amp; Founder</div>
<div class="rv-card" style="left:804px">Lorem ipsum dolor sit amet, consect etur adipiscing elit, sed do eiusmod tempor incididunt ut labore et dolore magna aliqua.Lorem ipsum dolor sit amet.</div>
<div class="rv-quote" style="left:1044px">&#8220;</div>

<div class="btn" style="left:524px;top:3715px;width:150px;height:47px;font-size:14px">VIEW MORE</div>

<!-- footer -->
<svg class="abs" style="left:0;top:3822px" width="1200" height="212" viewBox="0 0 1200 212">
  <path d="M0,205 C220,100 480,10 720,22 C930,32 1100,110 1200,150 L1200,212 L0,212 Z" fill="#0b2650"/>
  <path d="M0,168 C130,110 280,60 420,40 C290,72 140,128 0,210 Z" fill="#2a9df4"/>
  <path d="M1000,60 C1090,95 1150,125 1200,148 L1200,120 C1140,98 1080,78 1000,60 Z" fill="#2a9df4"/>
</svg>
<div class="abs footer"></div>
<div class="abs" style="left:115px;top:4066px;color:#fff;font-size:19px;font-weight:700">Coral Basin Pool Service</div>
<p class="abs" style="left:114px;top:4124px;width:280px;color:#fff;font-size:14.5px;line-height:24px">We have 14+ years experience Helping you overcome technology challenges</p>
<div class="social" style="left:115px"></div>
<div class="social" style="left:156px"></div>
<div class="social" style="left:197px"></div>
<div class="social" style="left:239px"></div>

<div class="ft-h" style="left:519px">Newsletter</div>
<p class="abs" style="left:519px;top:4100px;width:230px;color:#fff;font-size:11.5px;font-weight:600;line-height:24px">Subscribe to our newsletter to recieve updates or the latest news</p>
<div class="abs" style="left:519px;top:4185px;width:223px;height:41px;border-radius:4px;background:rgba(255,255,255,.22);color:#fff;font-size:12px;font-weight:600;display:flex;align-items:center;justify-content:space-between;padding:0 14px">Subscribe with us
  <svg width="18" height="14" viewBox="0 0 24 18" fill="none" stroke="#fff" stroke-width="2"><path d="M2 9h19M14 2l7 7-7 7"/></svg></div>

<div class="ft-h" style="left:862px">Contacts</div>
<svg class="abs" style="left:862px;top:4108px" width="32" height="32" viewBox="0 0 24 24" fill="none" stroke="#2a9df4" stroke-width="1.4"><path d="M22 16.9v3a2 2 0 0 1-2.2 2A19.8 19.8 0 0 1 2.1 4.2 2 2 0 0 1 4.1 2h3a2 2 0 0 1 2 1.7c.1.9.4 1.8.7 2.7a2 2 0 0 1-.5 2.1L8 9.8a16 16 0 0 0 6 6l1.3-1.3a2 2 0 0 1 2.1-.4c.9.3 1.8.6 2.7.7a2 2 0 0 1 1.7 2z"/></svg>
<div class="abs" style="left:910px;top:4097px;color:#fff;font-size:16px;font-weight:700">Contact Us</div>
<div class="abs" style="left:910px;top:4120px;color:#fff;font-size:14px">(44) 555-010-482</div>
<svg class="abs" style="left:862px;top:4175px" width="32" height="32" viewBox="0 0 24 24" fill="none" stroke="#2a9df4" stroke-width="1.4"><path d="M3 10l9-7 9 7v11H3z"/><path d="M3 10l9 6 9-6"/></svg>
<div class="abs" style="left:910px;top:4168px;color:#fff;font-size:16px;font-weight:700">Mail Us</div>
<div class="abs" style="left:910px;top:4192px;color:#fff;font-size:14px">info@coralbasin.example</div>

<div class="abs" style="left:0;top:4334px;width:1194px;text-align:center;color:#fff;font-size:13.5px;font-weight:600">Coral Basin Pool Service</div>
<div class="abs" style="left:1066px;top:4326px;width:32px;height:32px;background:var(--blue);display:flex;align-items:center;justify-content:center">
  <svg width="14" height="14" viewBox="0 0 24 24" fill="none" stroke="#fff" stroke-width="2"><path d="M12 21V4M5 11l7-7 7 7"/></svg>
</div>

</body>
</html>
```